Website design for dressage horse training business

Looking to develop a new website design for a dressage horse training website. We want to change from a single landing page to one with multiple pages.
You are free to use your creativity to design the main landing page. This is the only page you need to design at this point. I would encourage looking at other Dressage Training websites to get a feel for what is typically on them. A few websites are listed below although I think the design of them could be better.
Notes:
- Menu to include: Home, Services, News Room, Blog, About Us, Contact,
- FAQ section on main page
- Logo to remain the same - the logo attached is not the correct color so change to match existing color.
- Change 'Sponsors' to 'Partnerships' on main page
Here is the link to the current site:
https://larkvalebarn.com/
Example sites
https://www.quillbrookstablesna.com/
https://corinnahaldwickdressage.com/
Older women with disposable income

```html
<!DOCTYPE html>
<html lang="en">
<head>
<meta charset="utf-8">
<title>Larkvale Barn – Dressage &amp; Sport Horse Training</title>
<link href="https://fonts.googleapis.com/css2?family=Khand:wght@400;500;600&family=Poppins:wght@300;400;500;600&display=swap" rel="stylesheet">
<style>
:root{
  --tan:#c49a6c;
  --tan-dark:#a87d50;
  --ink:#1d1d1d;
  --muted:#8a8a8a;
  --line:#dcdcdc;
  --white:#ffffff;
  --paper:#f3f3f3;
  --dark:#2e2b28;
  --black:#111111;
}
*{box-sizing:border-box;margin:0;padding:0}
html,body{width:1200px;height:2938px;overflow:hidden;background:var(--paper)}
body{font-family:"Poppins",sans-serif;color:var(--ink)}
.stage{position:relative;width:1200px;height:2938px;overflow:hidden}
.page{position:absolute;left:210px;top:26px;width:1200px;height:4440px;transform:scale(.65);transform-origin:0 0;background:var(--white);box-shadow:0 10px 40px rgba(0,0,0,.12)}
.accent{color:var(--tan)}
.btn{display:inline-flex;align-items:center;gap:8px;height:34px;padding:0 24px;border-radius:17px;font-size:11px;text-transform:uppercase;letter-spacing:.5px;background:var(--tan);color:var(--white);white-space:nowrap}
.btn .dot{width:12px;height:12px;border-radius:50%;background:var(--white);opacity:.9}
.btn-ghost{background:transparent;border:1.5px solid var(--tan);color:var(--white)}
section{position:relative;overflow:hidden}
.photo{position:absolute}
/* hero */
.hero{height:635px;background:linear-gradient(100deg,#3b3526 0%,#4a3a28 40%,#5a3a22 70%,#3a2c22 100%)}
.hero .photo{inset:0;background:radial-gradient(ellipse at 72% 45%,rgba(120,60,25,.7),transparent 55%),linear-gradient(180deg,rgba(0,0,0,.15),rgba(0,0,0,.35))}
.topbar{position:absolute;left:140px;right:140px;top:28px;height:70px;display:flex;align-items:center;justify-content:space-between;color:var(--white);font-family:"Khand",sans-serif;font-size:15px;border-bottom:1px solid rgba(255,255,255,.35)}
.topbar .item{display:flex;align-items:center;gap:10px;width:200px}
.topbar .item:last-child{justify-content:flex-end}
.brand{font-family:"Khand",sans-serif;font-weight:500;font-size:40px;letter-spacing:1px;color:var(--tan);line-height:1;white-space:nowrap}
.nav{position:absolute;left:140px;right:140px;top:110px;height:44px;border-bottom:1px solid rgba(255,255,255,.35);display:flex;justify-content:center;gap:30px;font-family:"Khand",sans-serif;color:var(--white);font-size:15px;align-items:center}
.nav .on{border-bottom:2px solid var(--white);padding-bottom:2px}
.nav .search{position:absolute;right:60px;display:flex;gap:8px;align-items:center}
.hero-copy{position:absolute;left:140px;top:265px;color:var(--white)}
.hero-copy h1{font-family:"Khand",sans-serif;font-weight:400;font-size:80px;line-height:1;color:var(--tan)}
.hero-copy h2{font-family:"Khand",sans-serif;font-weight:400;font-size:42px;line-height:1.1}
.hero-copy p{font-size:17px;margin-top:8px}
.hero-copy .actions{display:flex;gap:28px;margin-top:28px}
.hero-copy .btn{height:36px;padding:0 30px}
/* section titles */
.title{text-align:center;font-family:"Khand",sans-serif;font-weight:600;font-size:44px;line-height:1}
.divider{display:flex;justify-content:center;align-items:center;gap:12px;margin-top:6px}
.divider i{display:block;width:80px;height:2px;background:var(--ink)}
.divider b{display:block;width:18px;height:18px;border-radius:50%;background:var(--tan)}
/* training */
.training{height:547px}
.training .title{margin-top:40px}
.train-intro{position:absolute;left:80px;top:230px;width:350px}
.train-intro small{font-family:"Khand",sans-serif;font-size:15px;color:var(--muted);text-transform:uppercase}
.train-intro h3{font-family:"Khand",sans-serif;font-weight:500;font-size:38px;line-height:1;margin:6px 0 30px}
.card{position:absolute;top:172px;width:318px;height:293px;border-radius:10px;background:var(--white);box-shadow:0 4px 18px rgba(0,0,0,.14);text-align:center;padding:42px 30px}
.card h4{font-family:"Poppins",sans-serif;font-weight:400;font-size:24px;display:inline-block;padding-bottom:8px;border-bottom:2px solid var(--tan)}
.card p{font-size:11px;line-height:1.65;margin:22px 0 26px;color:#555}
.card-lessons{left:474px}
.card-training{left:814px;background:var(--tan);color:var(--white)}
.card-training h4{border-color:var(--white)}
.card-training p{color:var(--white)}
.card-training .btn{background:var(--white);color:var(--tan)}
.card-training .btn .dot{background:var(--tan)}
/* about */
.about{height:540px;background:linear-gradient(180deg,#3e3b33,#2b2a27 55%,#3a342d)}
.about .photo-blob{left:168px;top:55px;width:310px;height:475px;border-radius:48% 52% 46% 54%/38% 40% 60% 62%;background:linear-gradient(160deg,#7d8d99,#6a4a32 60%,#4a3a2e)}
.about-copy{position:absolute;left:600px;top:108px;width:507px;color:var(--white)}
.about-copy h2{font-family:"Khand",sans-serif;font-weight:500;font-size:44px;line-height:1}
.about-copy p{font-size:14.5px;line-height:1.4;margin:16px 0 18px}
.about-copy .btn{height:34px;text-transform:none;font-family:"Khand",sans-serif;font-size:15px;padding:0 22px}
/* partnerships */
.partners{height:673px}
.partners .title{margin-top:40px}
.partner{position:absolute;top:154px;width:390px;height:430px;border:2px solid var(--tan);border-radius:4px;padding:10px}
.partner-inner{height:100%;background:var(--white);box-shadow:0 3px 14px rgba(0,0,0,.12);text-align:center;padding:42px 40px}
.partner .badge{width:140px;height:48px;margin:0 auto;border-radius:24px;background:var(--tan-dark)}
.partner .badge.sq{width:44px;height:44px;border-radius:4px;background:#555}
.partner h4{font-weight:500;font-size:22px;margin:22px 0 16px}
.partner p{font-size:13px;line-height:1.6;color:#333;margin-bottom:22px}
.partner .btn{height:32px}
.p1{left:181px}.p2{left:629px}
/* for sale */
.sale{height:569px;background:linear-gradient(180deg,#3d3935,#4a4038 60%,#6b4b2c)}
.sale .photo-horse{left:139px;top:77px;width:397px;height:419px;border-radius:6px;background:linear-gradient(180deg,#6e98b6 0%,#5f8a52 55%,#4a3425 100%)}
.sale-frame{position:absolute;left:486px;top:101px;width:578px;height:369px;border:2px solid var(--tan);border-radius:8px}
.sale-card{position:absolute;left:504px;top:113px;width:552px;height:345px;background:var(--white);border-radius:8px;padding:40px 56px}
.sale-card small{font-size:15px;color:var(--muted)}
.sale-card h3{font-family:"Khand",sans-serif;font-weight:600;font-size:44px;line-height:1.05}
.sale-card p{font-size:14px;line-height:1.7;color:var(--muted);margin:12px 0 26px}
/* faq */
.faq{height:644px}
.faq-copy{position:absolute;left:97px;top:105px;width:518px}
.faq-copy small{font-family:"Khand",sans-serif;font-size:21px}
.faq-copy h2{font-family:"Khand",sans-serif;font-weight:600;font-size:44px;line-height:1;margin-bottom:18px}
.faq-row{display:flex;justify-content:space-between;height:53px;align-items:center;border-bottom:1.5px solid var(--line);font-size:14px;color:#333;padding:0 10px 0 2px}
.faq-row:last-child{border-bottom:0}
.faq-row span{color:var(--tan);font-size:16px}
.faq .photo-faq{left:712px;top:95px;width:393px;height:432px;background:linear-gradient(180deg,#9fb2c3 0%,#7e93a6 55%,#5a4a3e 100%)}
/* contact */
.touch{height:501px;background:linear-gradient(120deg,#3a3a3a,#2b2b2b 60%,#1c1c1c);color:var(--white)}
.touch-info{position:absolute;left:141px;top:80px}
.touch-info h2{font-family:"Khand",sans-serif;font-weight:600;font-size:46px;line-height:1;margin-bottom:26px}
.touch-info h5{font-family:"Khand",sans-serif;font-weight:500;font-size:20px;line-height:1}
.touch-info p,.touch-info a{font-size:11.5px;line-height:1.5;color:var(--white);display:block}
.touch-info .group{margin-bottom:30px}
.touch-info a{text-decoration:underline}
.form{position:absolute;left:494px;top:160px;width:571px;font-size:11.5px}
.field{position:absolute;border-bottom:1px solid rgba(255,255,255,.6);height:26px}
.f-name{left:0;top:0;width:270px}.f-email{left:305px;top:0;width:266px}
.f-phone{left:0;top:48px;width:270px}.f-country{left:305px;top:48px;width:266px;display:flex;justify-content:space-between}
.f-msg{left:0;top:104px;width:571px;height:78px}
.form .btn{position:absolute;left:0;top:236px;height:32px;text-transform:none;font-size:12px}
/* footer */
.footer{position:relative;height:293px}
.foot-brand{position:absolute;left:84px;top:60px;width:250px}
.foot-brand p{font-size:10.5px;line-height:1.55;color:#444;margin-top:16px}
.foot-col{position:absolute;top:75px}
.foot-col h6{font-family:"Khand",sans-serif;font-weight:600;font-size:17px;margin-bottom:12px}
.foot-col li{list-style:none;font-size:11.5px;line-height:1.85}
.foot-col .ct{display:flex;gap:8px;font-size:11.5px;line-height:1.45;margin-bottom:8px}
.c1{left:443px}.c2{left:692px;width:230px}.c3{left:972px}
.social{display:flex;gap:14px}
.social i{display:block;width:22px;height:22px;border-radius:50%;border:2px solid var(--ink)}
.bar{height:38px;background:var(--black);color:var(--white);font-size:11px;display:flex;align-items:center;justify-content:center}
</style>
</head>
<body>
<div class="stage">
<div class="page">

  <section class="hero">
    <div class="photo" role="img" aria-label="Dressage rider in white gloves on a bay horse in an arena"></div>
    <div class="topbar">
      <div class="item">
        <svg width="16" height="22" viewBox="0 0 16 22"><path d="M8 0C3.6 0 0 3.5 0 7.8 0 13.5 8 22 8 22s8-8.5 8-14.2C16 3.5 12.4 0 8 0z" fill="#c49a6c"/><circle cx="8" cy="8" r="3" fill="#3b3526"/></svg>
        Iowa, USA
      </div>
      <div class="brand">Larkvale Barn</div>
      <div class="item">
        <svg width="18" height="18" viewBox="0 0 24 24"><path d="M6.6 10.8a15 15 0 0 0 6.6 6.6l2.2-2.2a1 1 0 0 1 1-.25 11.4 11.4 0 0 0 3.6.6 1 1 0 0 1 1 1V20a1 1 0 0 1-1 1A17 17 0 0 1 3 4a1 1 0 0 1 1-1h3.5a1 1 0 0 1 1 1c0 1.25.2 2.45.6 3.6a1 1 0 0 1-.25 1z" fill="#c49a6c"/></svg>
        515-555-0187
      </div>
    </div>
    <nav class="nav">
      <span class="on">Home</span><span>Services</span><span>News Room</span><span>Blog</span><span>About Us</span><span>Contact</span>
      <span class="search">Search
        <svg width="12" height="12" viewBox="0 0 12 12"><circle cx="5" cy="5" r="4" fill="none" stroke="#fff" stroke-width="1.5"/><path d="M8 8l3.5 3.5" stroke="#fff" stroke-width="1.5"/></svg>
      </span>
    </nav>
    <div class="hero-copy">
      <h1>Central Iowa's</h1>
      <h2>Premier dressage and sport horse training</h2>
      <p>Located outside Des Moines, Iowa</p>
      <div class="actions">
        <span class="btn">Services</span>
        <span class="btn btn-ghost">Contact Us</span>
      </div>
    </div>
  </section>

  <section class="training">
    <h2 class="title">Training &amp; <span class="accent">Lessons</span></h2>
    <div class="divider"><i></i><b></b><i></i></div>
    <div class="train-intro">
      <small>Our Traning</small>
      <h3>Get Start Your Lesson and Training</h3>
      <span class="btn">Get Started <span class="dot"></span></span>
    </div>
    <div class="card card-lessons">
      <h4>Lessons</h4>
      <p>Lessons are available for all ages of riders. Elise thoroughly enjoys working with accomplished riders looking to succeed in the show ring, as well as riders...</p>
      <span class="btn">Know More <span class="dot"></span></span>
    </div>
    <div class="card card-training">
      <h4>Training</h4>
      <p>Larkvale Barn offers both full and half time training options with Elise Varnell. There is much flexibility with both rides and/or lessons weekly in the training packages...</p>
      <span class="btn">Know More <span class="dot"></span></span>
    </div>
  </section>

  <section class="about">
    <div class="photo photo-blob" role="img" aria-label="Rider in a cap on a bay horse at a farm"></div>
    <div class="about-copy">
      <h2>ABOUT <span class="accent">US</span></h2>
      <p>International rider and trainer, Elise Varnell began her riding career at a young age. She went up through the ranks of a youth riding program with an emphasis and focus in eventing. During college, Elise worked for a small breeder starting young horses. Elise loves starting young horses including starting and guiding them in a correct and quiet way to help them flourish. Her training focuses on gymnastic training incorporating ground work/lunging/long lining, jumping, cavelletti and regular hacking and trail riding. Elise is a national silver medalist having competed through Intermediate II.</p>
      <span class="btn btn-ghost">Read more</span>
    </div>
  </section>

  <section class="partners">
    <h2 class="title">Partner<span class="accent">ships</span></h2>
    <div class="divider"><i></i><b></b><i></i></div>
    <div class="partner p1"><div class="partner-inner">
      <div class="badge"></div>
      <h4>Harrowgate Saddlery</h4>
      <p>Harrowgate Saddlery is constantly designing and researching saddles and riders to find the right blend of design and craftsmanship to fit today's demands. Every saddle's detail is carefully checked to be sure the workmanship and quality is there. All saddles are anatomically</p>
      <span class="btn">Learn More <span class="dot"></span></span>
    </div></div>
    <div class="partner p2"><div class="partner-inner">
      <div class="badge sq"></div>
      <h4>Whitlock's Saddlery</h4>
      <p>My goal is to provide the best possible fit for both horse and rider whether it is a saddle you already own, one you have on trial, or one that I carry. Being a qualified saddle fitter with a professional saddlers' guild allows me to work with all saddle types and brands. In</p>
      <span class="btn">Learn More <span class="dot"></span></span>
    </div></div>
  </section>

  <section class="sale">
    <div class="photo photo-horse" role="img" aria-label="Dark bay dressage horse performing a levade beside a white fence"></div>
    <div class="sale-frame"></div>
    <div class="sale-card">
      <small>For Sale</small>
      <h3>Marlow's <span class="accent">Promise</span></h3>
      <p>Marlow's Promise, "Finn," (Halcyon x Northern Quill) is a 2012, 16hh imported Hanoverian. Finn is an incredibly quiet and kind horse. He is ridden by both an amatuer and child rider. He loves to hack and is very quiet alone and with a group of horses. He has shown through first level with scores into the 70's at both training and first level</p>
      <span class="btn">Learn More <span class="dot"></span></span>
    </div>
  </section>

  <section class="faq">
    <div class="faq-copy">
      <small>What You Need To Know</small>
      <h2>Frequently Asked <span class="accent">Questions</span></h2>
      <div class="faq-row">What do you need to register your company <span>+</span></div>
      <div class="faq-row">Are there any hidden costs <span>+</span></div>
      <div class="faq-row">How many shares does a company need <span>+</span></div>
      <div class="faq-row">What happened after your company is registered <span>+</span></div>
      <div class="faq-row">how can I receive my cashback offer <span>+</span></div>
      <div class="faq-row">Can I set up a company on my own <span>+</span></div>
    </div>
    <div class="photo photo-faq" role="img" aria-label="Bay horse splashing through shallow water"></div>
  </section>

  <section class="touch">
    <div class="touch-info">
      <h2>Get In Touch</h2>
      <div class="group"><h5>Find Us</h5><p>48 Orchard Lane, Ankeny, IA 50021<br>United States</p></div>
      <div class="group"><h5>Get In Touch</h5><p>hello@larkvalebarn.com<br>+1 (515) 555-0142</p></div>
      <div class="group"><h5>Legal Stuff</h5><a>Privacy &amp; Policy</a><a>Terms &amp; Conditions</a></div>
    </div>
    <div class="form">
      <div class="field f-name">Name</div>
      <div class="field f-email">Email</div>
      <div class="field f-phone">Phone</div>
      <div class="field f-country">Country <span>⌄</span></div>
      <div class="field f-msg">Enter You Message</div>
      <span class="btn">Submit <span class="dot"></span></span>
    </div>
  </section>

  <footer>
    <div class="footer">
      <div class="foot-brand">
        <div class="brand" style="font-size:36px">Larkvale Barn</div>
        <p>Quiet, correct training for horses and riders at every level, from first lessons to the show ring, just outside Des Moines in central Iowa.</p>
      </div>
      <div class="foot-col c1">
        <h6>USEFULL LINKS</h6>
        <ul><li>Home</li><li>Services</li><li>News Room</li><li>Blog</li><li>About Us</li><li>Contact</li></ul>
      </div>
      <div class="foot-col c2">
        <h6>CONTACT US</h6>
        <div class="ct"><span>•</span>48 Orchard Lane, Ankeny, IA 50021</div>
        <div class="ct"><span>•</span>+1 (515) 555-0142</div>
        <div class="ct"><span>•</span>hello@larkvalebarn.com</div>
      </div>
      <div class="foot-col c3">
        <h6>SOCIAL LINKS</h6>
        <div class="social"><i></i><i></i><i></i></div>
      </div>
    </div>
    <div class="bar">© 2021 larkvalebarn.com. All Rights Reserved.</div>
  </footer>

</div>
</div>
</body>
</html>
```